M25 Billboard Advert Required Please

I need an advert for a motorway Billboard on the M25 , the advert should show the following in big letters:
GUTTER CLEANING
DALRYNFLUES.COM and a small logo off to the side (Our logo is attached)

The printer has requested the following (Important please) the advert has to be
pdf file / 300 dpi/landscape orientation / scaled to a minimum 25% advert size ( this particular site is 22ft x 10ft so 25% of this please). Please also make sure that the artwork is embedded and outlined correctly if this is incorrect it will affect the printing of the banner.

Target Market(s)

General Public

Industry/Entity Type

Gutter Cleaning

Requirements
Should not have
• No Change to our Logo

```html
<!DOCTYPE html>
<html lang="en">
<head>
<meta charset="utf-8">
<title>Gutter Cleaning Billboard</title>
<link href="https://fonts.googleapis.com/css2?family=Poppins:wght@600;700;800&display=swap" rel="stylesheet">
<style>
  :root {
    --brand-red: #b31e24;
    --band-black: #000000;
    --ink-white: #ffffff;
    --logo-ink: #1a1a1a;
    --logo-frame: #bdbdbd;
    --page-bg: #ffffff;
  }
  html, body {
    margin: 0;
    padding: 0;
    width: 1200px;
    height: 1200px;
    overflow: hidden;
    background: var(--page-bg);
  }
  .canvas {
    position: relative;
    width: 1200px;
    height: 1200px;
    display: flex;
    align-items: center;
    justify-content: center;
  }
  .billboard {
    display: block;
    width: 1120px;
    height: auto;
  }
  .headline {
    font-family: 'Poppins', sans-serif;
    font-weight: 700;
    fill: var(--ink-white);
  }
  .web-address {
    font-family: 'Poppins', sans-serif;
    font-weight: 700;
    fill: var(--ink-white);
  }
  .brand-name {
    font-family: 'Poppins', sans-serif;
    font-weight: 600;
    fill: var(--logo-ink);
  }
  .panel-red { fill: var(--brand-red); }
  .band-black { fill: var(--band-black); }
  .logo-box { fill: var(--ink-white); stroke: var(--logo-frame); stroke-width: 1; }
  .brand-square { fill: var(--brand-red); }
</style>
</head>
<body>
<main class="canvas">
  <svg class="billboard" viewBox="0 0 1052 488" xmlns="http://www.w3.org/2000/svg" aria-label="Gutter cleaning billboard advert">
    <rect class="panel-red" x="0" y="0" width="1052" height="385"/>
    <text class="headline" x="125" y="205" font-size="212" textLength="800" lengthAdjust="spacingAndGlyphs">GUTTER</text>
    <text class="headline" x="125" y="345" font-size="162" textLength="800" lengthAdjust="spacingAndGlyphs">CLEANING</text>

    <rect class="band-black" x="0" y="385" width="845" height="103"/>
    <text class="web-address" x="88" y="460" font-size="68" textLength="668" lengthAdjust="spacingAndGlyphs">DALRYNFLUES.COM</text>

    <rect class="logo-box" x="844.5" y="385.5" width="207" height="102"/>
    <rect class="brand-square" x="872" y="428" width="14" height="14"/>
    <text class="brand-name" x="894" y="442" font-size="19">Dalryn Flues</text>
  </svg>
</main>
</body>
</html>
```